Mobile dental anesthesiologist needs a postcard to market to other doctors

This postcard is intended to inform dentists in the California Central Coast region that I am available to travel to their office to serve their patient's anesthesia needs. It is important to know that other anesthesiologists are usually booked for weeks in advance and are very costly. Our market niche is greater availability and lower cost. I would prefer a 2 sided oversized postcard. The attached images are DIY projects I've done recently...You can see why I'm reaching out to professionals.

Industry/Entity Type

Dental

```html
<!DOCTYPE html>
<html lang="en">
<head>
<meta charset="utf-8">
<title>Harbor Ridge Dental Anesthesia – Postcard</title>
<link rel="stylesheet" href="https://fonts.googleapis.com/css2?family=Oswald:wght@400;500&family=Roboto+Condensed:wght@400;700&family=Montserrat:wght@500&display=swap">
<style>
  :root {
    --blue: #2a95d6;
    --green: #3f7f2c;
    --green-dark: #1f5b2a;
    --navy: #0f2540;
    --ink: #111111;
    --white: #ffffff;
    --bg: #e9e6e1;
    --rule: #9a9a9a;
  }
  * { margin: 0; padding: 0; box-sizing: border-box; }
  html, body { width: 1200px; height: 1000px; overflow: hidden; background: var(--bg); }
  body { position: relative; font-family: "Roboto Condensed", Arial, sans-serif; color: var(--ink); }

  .card { position: absolute; width: 635px; height: 460px; background: var(--white); overflow: hidden; box-shadow: 0 2px 6px rgba(0,0,0,.18); }
  .card--front { left: 30px; top: 22px; }
  .card--back { left: 517px; top: 506px; height: 462px; }
  .card__shapes { position: absolute; inset: 0; }

  .brand { position: absolute; display: flex; align-items: center; gap: 8px; font-family: "Oswald", sans-serif; font-weight: 400; color: var(--green); line-height: 1.05; }
  .brand__dot { width: 14px; height: 14px; border-radius: 50%; background: var(--green); flex: none; }
  .card--front .brand { left: 46px; top: 66px; font-size: 23px; }
  .card--back .brand { left: 412px; top: 360px; font-size: 24px; }

  .front__title { position: absolute; left: 19px; top: 140px; font-family: "Oswald", sans-serif; font-weight: 500; font-size: 28px; color: var(--white); letter-spacing: .3px; }
  .front__tagline { position: absolute; left: 19px; top: 176px; font-family: "Oswald", sans-serif; font-weight: 500; font-size: 19px; color: var(--navy); }
  .front__intro { position: absolute; left: 19px; top: 210px; width: 236px; font-size: 11.4px; line-height: 1.2; color: var(--white); text-align: justify; }
  .front__intro strong { font-weight: 700; }
  .front__rule { position: absolute; left: 19px; top: 302px; width: 236px; border-top: 1px dashed rgba(255,255,255,.85); }
  .front__cta { position: absolute; left: 22px; top: 313px; width: 245px; font-size: 15.5px; line-height: 1.2; color: var(--white); }

  .front__phone { position: absolute; left: 22px; top: 404px; display: flex; align-items: center; gap: 8px; font-family: "Montserrat", sans-serif; font-weight: 500; font-size: 31px; color: var(--ink); }
  .front__area { position: absolute; left: 330px; top: 397px; font-size: 10.5px; color: var(--ink); }
  .front__email { position: absolute; left: 330px; top: 414px; display: flex; align-items: center; gap: 5px; font-family: "Montserrat", sans-serif; font-size: 19.5px; color: var(--ink); }

  .back__title { position: absolute; left: 16px; top: 138px; font-family: "Oswald", sans-serif; font-weight: 500; font-size: 20.5px; color: var(--blue); }
  .back__text { position: absolute; left: 16px; top: 169px; width: 280px; font-size: 11px; line-height: 1.22; text-align: justify; }
  .back__text strong { font-weight: 700; }
  .benefits { position: absolute; left: 26px; top: 248px; width: 262px; height: 43px; border-radius: 5px; background: var(--blue); border: 2px solid #9fd0ef; outline: 1px solid var(--blue); color: var(--white); font-size: 11.4px; font-weight: 700; text-align: center; line-height: 1.15; padding-top: 6px; }
  .back__name { position: absolute; right: 426px; top: 311px; font-family: "Oswald", sans-serif; font-weight: 500; font-size: 24px; line-height: 1.2; text-align: right; color: var(--ink); }
  .back__phone { position: absolute; right: 427px; top: 380px; font-family: "Oswald", sans-serif; font-size: 19px; color: var(--blue); }
  .back__email { position: absolute; right: 427px; top: 407px; font-family: "Oswald", sans-serif; font-size: 19px; color: var(--blue); }
  .stamp-box { position: absolute; left: 525px; top: 27px; width: 78px; height: 92px; border: 1px solid #888; }
  .address-line { position: absolute; left: 346px; width: 262px; border-top: 1px solid var(--rule); }
  .address-line--first { top: 198px; }
  .address-line--second { top: 258px; }
</style>
</head>
<body>

<section class="card card--front">
  <svg class="card__shapes" viewBox="0 0 635 460" width="635" height="460">
    <rect x="0" y="124" width="275" height="256" fill="var(--blue)"/>
    <path d="M298,0 L635,0 L635,288 Q470,350 280,358 Q262,200 298,0 Z" fill="#555555" role="img" aria-label="Black and white portrait of the dentist anesthesiologist in a suit and tie"/>
    <path d="M298,0 Q262,200 280,358" fill="none" stroke="var(--green)" stroke-width="7"/>
    <path d="M0,372 Q330,378 635,284 L635,296 Q330,392 0,384 Z" fill="var(--green)"/>
  </svg>

  <div class="brand"><span class="brand__dot"></span><span>Harbor Ridge<br>Dental Anesthesia</span></div>

  <h1 class="front__title">DENTAL ANESTHESIA</h1>
  <p class="front__tagline">Opening Doors to Treatment</p>
  <p class="front__intro">Put your patients and their families at ease by offering safe and effective anesthesia. <strong>Dr. Evan Hale is a Dentist Anesthesiologist</strong> with experience in treating patients with a wide spectrum of ages and conditions.</p>
  <div class="front__rule"></div>
  <p class="front__cta">Call to schedule a discussion of how Anesthesia may benefit your practice.</p>

  <div class="front__phone">
    <svg width="22" height="26" viewBox="0 0 24 28"><path d="M6 2 L10 8 L7.5 11 Q9 16 13 19.5 L16 17 L21 21 L18 25 Q10 25 5 17 Q1 9 6 2 Z" fill="var(--blue)"/><path d="M15 6 Q19 8 20 12 M15 2 Q22 5 23 12" fill="none" stroke="var(--blue)" stroke-width="1.6"/></svg>
    <span>555.014.2280</span>
  </div>
  <p class="front__area">Serving the Harbor Ridge region from Bayview to Millbrook</p>
  <div class="front__email">
    <svg width="20" height="15" viewBox="0 0 20 15"><rect x="1" y="1" width="18" height="13" fill="none" stroke="var(--blue)" stroke-width="1.6"/><path d="M1 1 L10 8 L19 1" fill="none" stroke="var(--blue)" stroke-width="1.6"/></svg>
    <span>evanhale@example.com</span>
  </div>
</section>

<section class="card card--back">
  <svg class="card__shapes" viewBox="0 0 635 462" width="635" height="462">
    <defs>
      <linearGradient id="sceneTone" x1="0" y1="0" x2="0" y2="1">
        <stop offset="0" stop-color="#e7b07a"/>
        <stop offset=".45" stop-color="#b08aa0"/>
        <stop offset=".75" stop-color="#3f4f8a"/>
        <stop offset="1" stop-color="#2b3a3a"/>
      </linearGradient>
    </defs>
    <rect x="0" y="0" width="350" height="126" fill="url(#sceneTone)" role="img" aria-label="Coastal town at sunset with palm trees and mountains"/>
    <path d="M352,0 L362,0 Q336,120 342,240 Q350,360 410,462 L398,462 Q338,360 330,240 Q325,120 352,0 Z" fill="var(--blue)"/>
    <path d="M362,0 L370,0 Q346,120 352,240 Q360,360 420,462 L410,462 Q350,360 342,240 Q336,120 362,0 Z" fill="var(--green-dark)"/>
    <circle cx="296" cy="366" r="68" fill="#c9dde6" stroke="var(--green-dark)" stroke-width="4" role="img" aria-label="Smiling dentist treating a young patient in the chair"/>
  </svg>

  <h2 class="back__title">How Do I Make My Appointment?</h2>
  <p class="back__text">We will make arrangements with your dentist or specialist depending on your treatment plan. Expect a call from <strong>Dr. Hale</strong> after you've scheduled with your office. On this call, we will discuss your medical history, what to expect, and how to prepare for your appointment.</p>
  <div class="benefits">YOUR DENTIST • YOUR OFFICE • EXPERT CARE<br>HOSPITAL STANDARDS • LOWER COST</div>

  <p class="back__name">Harbor Ridge<br>Dental Anesthesia</p>
  <p class="back__phone">555.014.2280</p>
  <p class="back__email">evanhale@example.com</p>

  <div class="stamp-box"></div>
  <div class="address-line address-line--first"></div>
  <div class="address-line address-line--second"></div>

  <div class="brand"><span class="brand__dot"></span><span>Harbor Ridge<br>Dental Anesthesia</span></div>
</section>

</body>
</html>
```